Peachynova.com adult webpage with links to various sites she is on.

UPDATE 3/10- let’s keep this a bit more simple. I am uploading three pics and a sketch of how she wants her site to look. It’s really just a page that has her links.

Looking to set up a homepage for my hot wife that has her clickable links on there. Pehaps a space for an about me and some notes encouraging audience to click and join velvet door.
Paqora link:

https://velvetdoorclub.com/away?url=https://Paqora.com/peachynova

Here is some
Copy from her:
“Queen of Dirty Talk” is important to work in.
🔥HOTWIFE SUPER SLUT🔥

...... I do things the other girls don’t! I suck and fuck like no other woman you’ll ever see. Filthy dirty talk, lots of sloppy oral, fantasy role play, dress up and cum swallowing.

Cum watch me! Have your mind..... and your big fat load blown away!

💋This page is where you will find ALL my links. My free velvetdoor has my videos for sale. My VIP page you will get the same videos at a discounted prices, plus lots of juicy extras. I also answer all my messages there. Make sure to check out my VIP page today so you don’t miss out on any of the fun!💋💋💋
Updates

I am tryin go to extend the project time to at least two weeks. I just don’t know how to edit. I have an email out to support.

Target Market(s)

Adult entertainment

Industry/Entity Type

Porn

Coding

Coded - Design and coding required

Number of Pages Required

1 page

Colors
000000
eea4c8

Requirements
Must have
• PeachyNova (no space between) is her stage name.
She would like maybe some cute horns in the logo. Maybe make the “S” have little devil horns on top and roll the bottom of the “S” like a devil tail with the arrows/spade point at at end.
A hot pic of her in background.
Buttons to her various pages.
Nice to have
• Perhaps an about me drop down or window we can write copy for? Pink black and leopard are good color choices.

```html
<!DOCTYPE html>
<html lang="en">
<head>
<meta charset="utf-8">
<title>PeachyNova</title>
<link rel="stylesheet" href="https://fonts.googleapis.com/css2?family=Roboto:wght@400;500;700&family=Parisienne&display=swap">
<style>
  :root {
    --pink: #eea4c8;
    --black: #000000;
    --ink: #1f1f1f;
    --muted: #8a8a8a;
    --white: #ffffff;
    --card-a: #f2f2f2;
    --card-b: #dfe6f2;
    --card-c: #f4e3d6;
    --card-d: #e4eef6;
  }
  * { box-sizing: border-box; margin: 0; padding: 0; }
  html, body { width: 1200px; height: 2900px; overflow: hidden; }
  body { position: relative; background: var(--white); font-family: "Roboto", Arial, sans-serif; color: var(--ink); }
  .abs { position: absolute; }

  /* Header */
  .site-header { left: 0; top: 0; width: 1200px; height: 72px; background: var(--white); }
  .brand { left: 24px; top: 10px; display: flex; flex-direction: column; align-items: center; gap: 4px; }
  .brand-dot { width: 28px; height: 28px; border-radius: 50%; background: var(--pink); }
  .brand-name { font-size: 12px; font-weight: 700; letter-spacing: 1px; color: var(--ink); }
  .main-nav { right: 160px; top: 27px; display: flex; gap: 44px; font-size: 15px; font-weight: 700; }
  .main-nav a { color: var(--ink); text-decoration: none; }
  .main-nav a.is-current { color: var(--pink); border-bottom: 2px solid var(--pink); padding-bottom: 4px; }
  .search-icon { left: 1090px; top: 28px; }

  /* Hero */
  .hero { left: 0; top: 72px; width: 1200px; height: 648px; }
  .hero-photo { width: 100%; height: 100%;
    background:
      radial-gradient(ellipse 520px 300px at 330px 300px, rgba(235,235,235,.75), rgba(235,235,235,0) 70%),
      radial-gradient(ellipse 600px 260px at 720px 420px, rgba(200,200,200,.6), rgba(200,200,200,0) 70%),
      linear-gradient(180deg, #5a5a5a 0%, #9c9c9c 45%, #b8b8b8 70%, #6e6e6e 100%); }
  .hero-title { left: 680px; top: 250px; font-family: "Parisienne", cursive; font-weight: 400; font-size: 96px; color: var(--pink); }

  /* About */
  .about-photo { left: 0; top: 720px; width: 592px; height: 592px;
    background:
      radial-gradient(ellipse 230px 280px at 300px 330px, #e3c4b4 0%, #c79f8c 45%, rgba(140,110,95,0) 80%),
      linear-gradient(90deg, #8c7a70 0%, #b8a59a 50%, #7d6c63 100%); }
  .about-text { left: 636px; top: 872px; width: 520px; }
  .script-heading { font-family: "Parisienne", cursive; color: var(--pink); font-weight: 400; }
  .about-text h2 { font-size: 52px; margin-bottom: 20px; }
  .about-text p { font-size: 13px; line-height: 1.6; color: var(--muted); margin-bottom: 14px; }

  /* Sections */
  .section-heading { left: 0; width: 1200px; text-align: center; font-size: 52px; }
  .feature { width: 248px; }
  .feature-photo { width: 248px; height: 226px; }
  .feature-label { margin-top: 14px; text-align: center; font-size: 16px; font-weight: 700; color: var(--ink); white-space: nowrap; }

  .video { width: 332px; }
  .video-thumb { position: relative; width: 332px; height: 240px; overflow: hidden; }
  .video-ribbon { position: absolute; left: 0; top: 0; }
  .video-play { position: absolute; left: 146px; top: 100px; }
  .video-caption { margin-top: 14px; font-size: 15px; font-weight: 700; line-height: 1.45; color: var(--ink); }

  .view-all { left: 520px; top: 2544px; width: 160px; height: 42px; background: var(--pink); color: var(--white); font-size: 14px; font-weight: 500; letter-spacing: 1px; display: flex; align-items: center; justify-content: center; text-decoration: none; }

  /* Footer */
  .site-footer { left: 0; top: 2688px; width: 1200px; height: 212px; background: var(--black); }
  .footer-nav { left: 0; top: 64px; width: 1200px; display: flex; justify-content: center; gap: 44px; font-size: 15px; font-weight: 700; }
  .footer-nav a { color: var(--white); text-decoration: none; }
  .payment-row { left: 0; top: 128px; width: 1200px; display: flex; justify-content: center; gap: 8px; }
  .payment-chip { width: 36px; height: 22px; border-radius: 3px; }
  .copyright { left: 0; top: 168px; width: 1200px; text-align: center; font-size: 12px; color: var(--white); }
  .chat-box { left: 0; top: 2856px; width: 288px; height: 44px; background: var(--white); border-radius: 4px 4px 0 0; display: flex; align-items: center; gap: 10px; padding: 0 12px; font-size: 12px; color: var(--muted); }
  .chat-dot { width: 18px; height: 18px; border-radius: 50%; background: var(--pink); }
</style>
</head>
<body>

<header class="site-header abs">
  <div class="brand abs">
    <span class="brand-dot"></span>
    <span class="brand-name">PEACHYNOVA</span>
  </div>
  <nav class="main-nav abs">
    <a class="is-current" href="#">Home</a>
    <a href="#">About Me</a>
    <a href="#">Watch My Videos</a>
    <a href="#">VIP</a>
    <a href="#">Blog</a>
    <a href="#">Contact Us</a>
  </nav>
  <svg class="search-icon abs" width="16" height="16" viewBox="0 0 16 16" aria-label="Search">
    <circle cx="6.5" cy="6.5" r="5" fill="none" stroke="#222" stroke-width="2"/>
    <line x1="10.2" y1="10.2" x2="15" y2="15" stroke="#222" stroke-width="2"/>
  </svg>
</header>

<section class="hero abs">
  <div class="hero-photo" role="img" aria-label="Black and white photo of the model lying on a bed"></div>
  <h1 class="hero-title abs">PeachyNova</h1>
</section>

<section>
  <div class="about-photo abs" role="img" aria-label="Close-up portrait photo of the model"></div>
  <div class="about-text abs">
    <h2 class="script-heading">About Me</h2>
    <p>“Queen of Dirty Talk” is important to work in.<br>HOTWIFE SUPER SLUT</p>
    <p>...... I do things the other girls don’t! I suck and fuck like no other woman you’ll ever see. Filthy dirty talk, lots of sloppy oral, fantasy role play, dress up and cum swallowing.</p>
    <p>Cum watch me! Have your mind..... and your big fat load blown away!</p>
  </div>
</section>

<h2 class="section-heading script-heading abs" style="top:1404px;">Hotwife super slut</h2>

<div class="feature abs" style="left:88px; top:1488px;">
  <div class="feature-photo" style="background:radial-gradient(ellipse 100px 130px at 124px 100px,#e2b29a,rgba(226,178,154,0) 80%),linear-gradient(160deg,#b98a6e,#6e4434);" role="img" aria-label="Photo of the model for filthy dirty talk"></div>
  <p class="feature-label">Filthy Dirty Talk</p>
</div>
<div class="feature abs" style="left:344px; top:1488px;">
  <div class="feature-photo" style="background:radial-gradient(ellipse 90px 140px at 130px 120px,#3a3a3a,rgba(58,58,58,0) 80%),linear-gradient(160deg,#f0ebe6,#b5a9a0);" role="img" aria-label="Photo of the model for sloppy oral"></div>
  <p class="feature-label">Lots Of Sloppy Oral</p>
</div>
<div class="feature abs" style="left:604px; top:1488px;">
  <div class="feature-photo" style="background:radial-gradient(ellipse 80px 150px at 120px 110px,#d8b49a,rgba(216,180,154,0) 80%),linear-gradient(160deg,#a88f73,#4e3a2c);" role="img" aria-label="Photo of the model for fantasy role play"></div>
  <p class="feature-label">Fantasy Role Play</p>
</div>
<div class="feature abs" style="left:860px; top:1488px;">
  <div class="feature-photo" style="background:radial-gradient(ellipse 120px 110px at 124px 120px,#e9b0a8,rgba(233,176,168,0) 80%),linear-gradient(160deg,#f1ece8,#c49a92);" role="img" aria-label="Photo of the model for dress up"></div>
  <p class="feature-label">Dress Up And Cum Swallowing</p>
</div>

<h2 class="section-heading script-heading abs" style="top:1828px;">My Videos</h2>

<div class="video abs" style="left:88px; top:1908px;">
  <div class="video-thumb" style="background:radial-gradient(ellipse 120px 140px at 170px 120px,#e8cdb0,rgba(232,205,176,0) 80%),linear-gradient(150deg,#cdb595,#7e6350);" role="img" aria-label="Video preview of the model">
    <svg class="video-ribbon" width="64" height="64"><polygon points="0,0 64,0 0,64" fill="#eea4c8"/></svg>
    <svg class="video-play" width="40" height="40"><circle cx="20" cy="20" r="18" fill="none" stroke="#fff" stroke-width="2"/><polygon points="16,12 29,20 16,28" fill="#fff"/></svg>
  </div>
  <p class="video-caption">Lorem ipsum dolor sit amet, consectetur adipiscing elit, sed do eiusmod</p>
</div>
<div class="video abs" style="left:432px; top:1908px;">
  <div class="video-thumb" style="background:radial-gradient(ellipse 120px 140px at 170px 110px,#e0e0e0,rgba(224,224,224,0) 80%),linear-gradient(150deg,#bdbdbd,#3e3e3e);" role="img" aria-label="Black and white video preview of the model">
    <svg class="video-ribbon" width="64" height="64"><polygon points="0,0 64,0 0,64" fill="#eea4c8"/></svg>
    <svg class="video-play" width="40" height="40"><circle cx="20" cy="20" r="18" fill="none" stroke="#fff" stroke-width="2"/><polygon points="16,12 29,20 16,28" fill="#fff"/></svg>
  </div>
  <p class="video-caption">Lorem ipsum dolor sit amet, consectetur adipiscing elit, sed do eiusmod</p>
</div>
<div class="video abs" style="left:776px; top:1908px;">
  <div class="video-thumb" style="background:radial-gradient(ellipse 150px 120px at 160px 150px,#e7a58e,rgba(231,165,142,0) 80%),linear-gradient(150deg,#c98a6f,#7d4232);" role="img" aria-label="Video preview of the model">
    <svg class="video-ribbon" width="64" height="64"><polygon points="0,0 64,0 0,64" fill="#eea4c8"/></svg>
    <svg class="video-play" width="40" height="40"><circle cx="20" cy="20" r="18" fill="none" stroke="#fff" stroke-width="2"/><polygon points="16,12 29,20 16,28" fill="#fff"/></svg>
  </div>
  <p class="video-caption">Lorem ipsum dolor sit amet, consectetur adipiscing elit, sed do eiusmod</p>
</div>

<div class="video abs" style="left:88px; top:2220px;">
  <div class="video-thumb" style="background:radial-gradient(ellipse 130px 120px at 170px 120px,#9a8c6c,rgba(154,140,108,0) 80%),linear-gradient(150deg,#7a6e52,#38352a);" role="img" aria-label="Video preview of the model">
    <svg class="video-ribbon" width="64" height="64"><polygon points="0,0 64,0 0,64" fill="#eea4c8"/></svg>
    <svg class="video-play" width="40" height="40"><circle cx="20" cy="20" r="18" fill="none" stroke="#fff" stroke-width="2"/><polygon points="16,12 29,20 16,28" fill="#fff"/></svg>
  </div>
  <p class="video-caption">Lorem ipsum dolor sit amet, consectetur adipiscing elit, sed do eiusmod</p>
</div>
<div class="video abs" style="left:432px; top:2220px;">
  <div class="video-thumb" style="background:radial-gradient(ellipse 110px 140px at 166px 120px,#e2bfa6,rgba(226,191,166,0) 80%),linear-gradient(150deg,#a98a6e,#5e4636);" role="img" aria-label="Video preview of the model">
    <svg class="video-ribbon" width="64" height="64"><polygon points="0,0 64,0 0,64" fill="#eea4c8"/></svg>
    <svg class="video-play" width="40" height="40"><circle cx="20" cy="20" r="18" fill="none" stroke="#fff" stroke-width="2"/><polygon points="16,12 29,20 16,28" fill="#fff"/></svg>
  </div>
  <p class="video-caption">Lorem ipsum dolor sit amet, consectetur adipiscing elit, sed do eiusmod</p>
</div>
<div class="video abs" style="left:776px; top:2220px;">
  <div class="video-thumb" style="background:radial-gradient(ellipse 90px 140px at 130px 130px,#dcb7a6,rgba(220,183,166,0) 80%),linear-gradient(150deg,#eee8e2,#a6968a);" role="img" aria-label="Video preview of the model">
    <svg class="video-ribbon" width="64" height="64"><polygon points="0,0 64,0 0,64" fill="#eea4c8"/></svg>
    <svg class="video-play" width="40" height="40"><circle cx="20" cy="20" r="18" fill="none" stroke="#fff" stroke-width="2"/><polygon points="16,12 29,20 16,28" fill="#fff"/></svg>
  </div>
  <p class="video-caption">Lorem ipsum dolor sit amet, consectetur adipiscing elit, sed do eiusmod</p>
</div>

<a class="view-all abs" href="#">VIEW ALL</a>

<footer class="site-footer abs">
  <nav class="footer-nav abs">
    <a href="#">Home</a>
    <a href="#">About Me</a>
    <a href="#">Watch My Videos</a>
    <a href="#">VIP</a>
    <a href="#">Blog</a>
    <a href="#">Contact Us</a>
  </nav>
  <div class="payment-row abs" aria-label="Accepted payment cards">
    <span class="payment-chip" style="background:var(--card-a);"></span>
    <span class="payment-chip" style="background:var(--card-b);"></span>
    <span class="payment-chip" style="background:var(--card-c);"></span>
    <span class="payment-chip" style="background:var(--card-d);"></span>
  </div>
  <p class="copyright abs">© Copyright 2021. The Company Name All Rights Reserved</p>
</footer>

<div class="chat-box abs">
  <span class="chat-dot"></span>
  <span>Type message</span>
</div>

</body>
</html>
```